website for local kavenda practicioner and yoga teacher trainer

The website should function primarily as:
A place where people can discover Kavenda and book sessions.
A central hub connecting all of my work.
A professional home that reflects my personality and approach.
Website design for Liesbet Oonwerk — Kavenda® Structural Integration practitioner, movement educator, yoga teacher and teacher trainer.
A website that can grow with future projects.
The website should feel: Warm, Human, Invitational, Professional, Accessible, Intelligent, Calm, Clear, Playful, Exploratory, Trustworthy
Avoid: New age aesthetics, Mystical clichés, Excessive spirituality, ”Guru" vibes, Overly clinical design, Corporate wellness branding, Busy layouts
Think: modern, grounded, curious and real.
My work combines three interconnected areas:
1.Bodywork: Touch, structure, awareness and one-on-one support.
2. Movement: Yoga, Pilates and embodied movement.
3. Education: Teacher trainings, workshops and continued learning.
Underlying values:
Curiosity over certainty
Possibility over perfection
Complexity without overwhelm
Science and lived experience together
Exploration rather than dogma
Human beings before methods
The primary goal of the website is to introduce people to Kavenda® Structural Integration and make it easy for them to:
Understand what Kavenda is
Discover whether it might be relevant for them
Learn what to expect from a session
Book an appointment
Booking should always feel visible and easy.
Secondary Goal: Present all other aspects of my work in one coherent place:
Yoga classes
Pilates classes
Teacher trainings
Workshops
Retreats
One-on-one movement sessions
Collaborations with studios
Website Structure
1: HOME
1.1.Hero Section: Large welcoming image
1.2 Two Main Pathways
- Bodywork: Kavenda® Structural Integration
- Movement & Education: Yoga, Pilates, trainings, workshops and retreats
- About Preview: Small introduction with portrait. + Button:
Read More
1.3 Current Events / What's Coming Up: Upcoming trainings, workshops and retreats. (This section should be easy to update)
1.4. Contact / Newsletter: Simple contact information
2: Kavenda® Structural Integration
What is Kavenda?
For whom is it?
What does a session look like?
FAQ
Prices
Booking
Future possibility:
Kaven Movement sessions
3: Movement
- Introductory text.
- Studio Classes (link to “my home base” - > local yoga studio)
- One-to-One Sessions: booking option (this is small; not a key aspect I want to promote)
- Workshops/ Retreats / Teacher Trainings => This section should be flexible and easy to update. Visitors should be able to click into specific offerings.
4. Events
Dynamic page for: Teacher trainings, Retreats, Workshops (see section in movement; here more elaborate)
Each event should contain: Image, Short description, Location, Date, Button for more information. (Linking to hosting studio/location)
5. Work With Me
For studios, organisations and teacher training schools.
Examples: Guest teaching, Workshops, Anatomy, Sequencing, Teacher development , Continuing education -> Clear call-to-action.
Call to action!!=> Book a Session
Prominent button in the navigation.
Footer:
- About Me: Longer biography (6th page)
Personal story and background.
- Testimonials (7th page): Separate page containing testimonials from:
Kavenda clients
Students
Teacher trainees
- Contact: 8th page
Visual Direction
Natural textures. Lots of white space.Editorial feeling.Professional photography.Simple navigation.
Less "wellness influencer.” More:Thoughtful, Contemporary, Timeless, Grounded, Human
Photography should show:
Teaching
Hands-on work
Natural movement
Real interaction
Simplicity
Avoid stereotypical yoga imagery and overly spiritual aesthetics.
Keywords
Warm. Curious. Human. Professional. Embodied. Intelligent. Accessible. Playful. Grounded. Exploratory. Real.
Inspiration / Core Message
Helping people feel more at home in their bodies through touch, movement and education.
The website should communicate that these are not separate services, but different expressions of the same intention:
Bodywork • Movement • Education.
Colours:
light orange/beige: e3d5c4
light orange/off white: f9f7f3
gray azure: 556b78
orange: d07b5a
grey orange: c09f80
dark grey: 3e3e3e
dark gray cyan 2f4f4f
gray green colour: a7c4a0
Fonts: Montserrat and Poppins + raleway
In added documents a try out idea of a website + logo. I will mainly use the logo with diffrent colours (image next to text).
My audience consists of people who want to feel more at home in their bodies and who appreciate a thoughtful, grounded and human approach to movement, touch and education. (30-65yo)
wellbeing
5+ page
- montserrat, poppins, raleway

```html
<!DOCTYPE html>
<html lang="en">
<head>
<meta charset="utf-8">
<title>Liesbet Oonwerk — Booking &amp; Pricing</title>
<link href="https://fonts.googleapis.com/css2?family=Cormorant+Garamond:wght@500;600&family=Montserrat:wght@500;600;700&family=Poppins:wght@400;500&display=swap" rel="stylesheet">
<style>
:root{
  --bg:#f8f3ee;
  --card:#f6eee7;
  --card-warm:#f3e7dd;
  --line:#e8dbd0;
  --ink:#1f3542;
  --text:#2b2b2b;
  --muted:#5a5a5a;
  --accent:#b7441f;
  --accent-soft:#efe2d8;
  --navy:#1f3a47;
}
*{box-sizing:border-box;margin:0;padding:0}
html,body{width:1200px;height:2234px;overflow:hidden}
body{background:var(--bg);font-family:"Poppins",sans-serif;color:var(--text);position:relative}
.serif{font-family:"Cormorant Garamond",serif}
.label{font-family:"Montserrat",sans-serif;font-weight:700;font-size:9.5px;letter-spacing:1.4px;text-transform:uppercase;color:var(--accent)}
.abs{position:absolute}
svg{display:block}

/* header */
.site-header{left:0;top:0;width:1200px;height:82px}
.brand{left:32px;top:16px;display:flex;align-items:center;gap:10px}
.brand-dot{width:40px;height:40px;border-radius:50%;background:var(--navy)}
.brand-name{font-family:"Cormorant Garamond",serif;font-weight:600;font-size:25px;color:var(--ink);line-height:1}
.brand-tag{font-family:"Montserrat",sans-serif;font-weight:600;font-size:7.5px;letter-spacing:.6px;color:var(--ink);margin-top:6px;text-transform:uppercase}
.main-nav{left:451px;top:36px;display:flex;gap:0}
.main-nav a{font-family:"Montserrat",sans-serif;font-weight:700;font-size:10px;letter-spacing:1px;color:var(--ink);text-decoration:none;text-transform:uppercase}

/* hero */
.hero-copy{left:91px;top:150px;width:420px}
.hero-title{font-family:"Cormorant Garamond",serif;font-weight:500;font-size:52px;line-height:60px;color:var(--ink);margin-top:26px}
.hero-title span{color:var(--accent)}
.rule{width:70px;height:2px;background:var(--accent);margin:30px 0 34px}
.hero-text{font-size:12.5px;line-height:27px;color:var(--text);width:300px}
.hero-photo{left:563px;top:81px;width:600px;height:439px;border-radius:4px;background:linear-gradient(100deg,#f4e6d8 0%,#e7c3a0 40%,#b7653a 65%,#e9d3bd 100%)}

/* section heads */
.section-head{left:0;width:1200px;text-align:center}
.section-title{font-family:"Cormorant Garamond",serif;font-weight:500;font-size:31px;color:var(--ink);margin-top:8px;line-height:1.2}
.section-sub{font-size:12px;color:var(--text);margin-top:6px;line-height:21px}

/* pricing cards */
.price-card{background:var(--card);border:1px solid var(--line);border-radius:6px;text-align:center}
.icon-circle{width:70px;height:70px;border-radius:50%;background:var(--accent-soft);margin:0 auto;display:flex;align-items:center;justify-content:center}
.icon-circle.sm{width:62px;height:62px}
.card-name{font-family:"Cormorant Garamond",serif;font-weight:500;font-size:21px;color:var(--accent);line-height:26px}
.card-price{font-family:"Cormorant Garamond",serif;font-weight:500;font-size:40px;color:var(--ink);line-height:1}
.mini-rule{width:32px;height:2px;background:var(--accent);margin:0 auto;opacity:.8}
.btn{display:inline-flex;align-items:center;justify-content:center;gap:9px;font-family:"Montserrat",sans-serif;font-weight:700;font-size:10.5px;letter-spacing:1.3px;text-transform:uppercase;border-radius:2px;text-decoration:none}
.btn-outline{border:1px solid var(--accent);color:var(--accent);background:transparent}
.btn-solid{background:var(--accent);color:#fff}
.includes{text-align:left;padding:0 0 0 46px}
.includes p{font-size:11px;font-weight:500;line-height:19px;color:var(--text)}
.includes ul{list-style:none;margin-top:8px}
.includes li{font-size:10.5px;line-height:24px;display:flex;align-items:center;gap:10px;white-space:nowrap}

.note{display:flex;gap:12px;font-size:11px;line-height:22px;color:var(--text)}

/* yoga cards */
.yoga-card{background:var(--card);border:1px solid var(--line);border-radius:6px;height:166px;padding:22px 24px}
.yoga-row{display:flex;gap:22px;align-items:flex-start;padding-left:2px}
.yoga-name{font-family:"Cormorant Garamond",serif;font-weight:500;font-size:16px;color:var(--ink)}
.yoga-price{font-family:"Cormorant Garamond",serif;font-weight:500;font-size:30px;color:var(--ink);margin-top:14px;line-height:1}
.yoga-card .mini-rule{margin:8px 0 0 0;width:14px}

/* cta band */
.cta-band{left:34px;top:1562px;width:1129px;height:230px;border-radius:6px;background:linear-gradient(90deg,#f3e4d8,#f0dfd1);overflow:hidden}
.cta-photo{position:absolute;right:0;top:0;width:510px;height:230px;background:linear-gradient(100deg,#eedfcf 0%,#c9a27b 40%,#e6d3be 70%,#d9c0a5 100%)}

/* events */
.event-card{background:#fbf7f3;border:1px solid var(--line);border-radius:4px;height:222px;overflow:hidden}
.event-img{height:67px}
.event-body{padding:12px 12px}
.event-date{font-family:"Montserrat",sans-serif;font-weight:700;font-size:8px;letter-spacing:1px;color:var(--accent)}
.event-title{font-family:"Cormorant Garamond",serif;font-weight:600;font-size:14.5px;color:var(--ink);margin-top:2px;white-space:nowrap}
.event-place{font-size:9px;display:flex;gap:6px;align-items:center;margin-top:6px}
.event-desc{font-size:8.8px;line-height:17px;margin-top:10px;white-space:nowrap}
.event-link{font-family:"Montserrat",sans-serif;font-weight:700;font-size:8.5px;letter-spacing:1px;color:var(--accent);margin-top:10px;display:flex;gap:8px;align-items:center;text-transform:uppercase}

/* newsletter / footer */
.divider{height:1px;background:var(--line)}
.email-field{left:502px;top:2075px;width:253px;height:32px;border:1px solid var(--line);background:#fbf8f5;border-radius:2px;font-size:10.5px;color:#888;padding:8px 14px}
.foot-col h4{font-family:"Montserrat",sans-serif;font-weight:700;font-size:8px;letter-spacing:1px;color:var(--ink)}
.foot-col li{list-style:none;font-size:9px;line-height:16.5px;color:var(--text)}
.social{width:28px;height:28px;border-radius:50%;border:1px solid #cfc3b8;display:flex;align-items:center;justify-content:center}
</style>
</head>
<body>

<header class="site-header abs">
  <div class="brand abs">
    <div class="brand-dot"></div>
    <div>
      <div class="brand-name">Liesbet Oonwerk</div>
      <div class="brand-tag">Bodywork · Movement · Education</div>
    </div>
  </div>
  <nav class="main-nav abs">
    <a href="#" style="margin-right:50px">Kavenda®</a>
    <a href="#" style="margin-right:44px">Movement</a>
    <a href="#" style="margin-right:43px">Events</a>
    <a href="#" style="margin-right:43px">Work with me</a>
    <a href="#" style="margin-right:43px">About</a>
    <a href="#">Contact</a>
  </nav>
</header>

<section class="hero">
  <div class="hero-copy abs">
    <div class="label">Booking &amp; Pricing</div>
    <h1 class="hero-title">Invest in yourself.<br>Feel the difference<span>.</span></h1>
    <div class="rule"></div>
    <p class="hero-text">Kavenda® Structural Integration, movement<br>and yoga offerings to support your<br>body, mind and life.</p>
  </div>
  <div class="hero-photo abs" role="img" aria-label="Photo of the practitioner sitting relaxed on a wooden floor in warm sunlight beside a potted plant"></div>
</section>

<section>
  <div class="section-head abs" style="top:551px">
    <div class="label">Kavenda® Structural Integration</div>
    <h2 class="section-title">Sessions &amp; Packages</h2>
    <p class="section-sub">Choose the option that supports your journey.</p>
  </div>

  <div class="price-card abs" style="left:48px;top:655px;width:341px;height:507px;padding-top:26px">
    <div class="icon-circle"><svg width="30" height="30" viewBox="0 0 30 30" fill="none" stroke="#1f3542" stroke-width="1.4"><circle cx="15" cy="8" r="3"/><path d="M15 12v8M9 14c0 6 2 10 6 10s6-4 6-10"/></svg></div>
    <div class="card-name" style="margin-top:20px">Discovery Session</div>
    <div class="card-price" style="margin-top:16px">€40</div>
    <div class="mini-rule" style="margin-top:16px"></div>
    <div class="includes" style="margin-top:18px">
      <p>Perfect if you're unsure whether<br>Kavenda® is right for you.</p>
      <p style="margin-top:10px">This session includes:</p>
      <ul>
        <li><svg width="10" height="8" viewBox="0 0 10 8" fill="none" stroke="#b7441f" stroke-width="1.5"><path d="M1 4l3 3 5-6"/></svg>Getting to know each other</li>
        <li><svg width="10" height="8" viewBox="0 0 10 8" fill="none" stroke="#b7441f" stroke-width="1.5"><path d="M1 4l3 3 5-6"/></svg>A hands-on touch experience</li>
        <li><svg width="10" height="8" viewBox="0 0 10 8" fill="none" stroke="#b7441f" stroke-width="1.5"><path d="M1 4l3 3 5-6"/></svg>Exploring your motivation and expectations</li>
        <li><svg width="10" height="8" viewBox="0 0 10 8" fill="none" stroke="#b7441f" stroke-width="1.5"><path d="M1 4l3 3 5-6"/></svg>Discussing what's possible and the scope</li>
        <li><svg width="10" height="8" viewBox="0 0 10 8" fill="none" stroke="#b7441f" stroke-width="1.5"><path d="M1 4l3 3 5-6"/></svg>A supportive start to your journey.</li>
      </ul>
      <a class="btn btn-solid" href="#" style="width:232px;height:38px;margin-top:22px">Book on Slotwise <span>→</span></a>
    </div>
  </div>

  <div class="price-card abs" style="left:409px;top:655px;width:228px;height:432px;padding-top:60px">
    <div class="icon-circle sm"><svg width="26" height="26" viewBox="0 0 26 26" fill="none" stroke="#1f3542" stroke-width="1.4"><circle cx="13" cy="6" r="2.6"/><path d="M13 10v7M6 12l7 2 7-2M9 23l4-6 4 6"/></svg></div>
    <div class="card-name" style="margin-top:42px">Single Session</div>
    <div class="card-price" style="margin-top:38px">€90</div>
    <div class="mini-rule" style="margin-top:22px"></div>
    <a class="btn btn-outline" href="#" style="width:194px;height:40px;margin-top:70px">Book on Slotwise <span>→</span></a>
  </div>

  <div class="price-card abs" style="left:649px;top:655px;width:230px;height:432px;padding-top:60px">
    <div class="icon-circle sm"><svg width="28" height="20" viewBox="0 0 28 20" fill="none" stroke="#1f3542" stroke-width="1.4"><path d="M2 4c4-3 8 3 12 0s8-3 12 0M2 10c4-3 8 3 12 0s8-3 12 0M2 16c4-3 8 3 12 0s8-3 12 0"/></svg></div>
    <div class="card-name" style="margin-top:26px">Sessions 1–3<br>Package</div>
    <div class="card-price" style="margin-top:28px">€255</div>
    <div class="mini-rule" style="margin-top:22px"></div>
    <a class="btn btn-outline" href="#" style="width:194px;height:40px;margin-top:70px">Book on Slotwise <span>→</span></a>
  </div>

  <div class="price-card abs" style="left:899px;top:655px;width:239px;height:432px;padding-top:17px;background:var(--card-warm)">
    <div class="label" style="font-size:9px">Best value</div>
    <div class="icon-circle sm" style="margin-top:30px"><svg width="30" height="22" viewBox="0 0 30 22" fill="none" stroke="#1f3542" stroke-width="1.4"><path d="M8 16a7 7 0 0 1 14 0M3 17h24M15 2v4M5 7l3 3M25 7l-3 3"/></svg></div>
    <div class="card-name" style="margin-top:26px">Complete<br>Ten Series Package</div>
    <div class="card-price" style="margin-top:28px">€800</div>
    <div class="mini-rule" style="margin-top:22px"></div>
    <a class="btn btn-solid" href="#" style="width:202px;height:40px;margin-top:70px">Book on Slotwise <span>→</span></a>
  </div>

  <div class="note abs" style="left:418px;top:1118px">
    <svg width="16" height="16" viewBox="0 0 16 16" fill="none" stroke="#555" style="margin-top:3px"><circle cx="8" cy="8" r="7"/><path d="M8 7v4M8 4.5v.5"/></svg>
    <p>Sessions are 60 or 90 minutes. Prices include VAT where applicable.<br>Packages are valid for 6 months from the date of purchase.</p>
  </div>
</section>

<section>
  <div class="divider abs" style="left:91px;top:1204px;width:1009px"></div>
  <div class="abs" style="left:582px;top:1186px;width:36px;height:24px;background:var(--bg);display:flex;justify-content:center">
    <svg width="26" height="18" viewBox="0 0 26 18" fill="none" stroke="#b7441f" stroke-width="1.3"><path d="M13 16C9 12 10 5 13 2c3 3 4 10 0 14zM13 16C8 15 5 11 5 7c4 0 7 4 8 9zM13 16c5-1 8-5 8-9-4 0-7 4-8 9z"/></svg>
  </div>
  <div class="section-head abs" style="top:1224px">
    <div class="label">Yoga</div>
    <h2 class="section-title" style="font-size:28px">Private Sessions</h2>
    <p class="section-sub" style="font-size:11.5px">One-to-one yoga sessions tailored to your body,<br>goals and practice.</p>
  </div>

  <div class="yoga-card abs" style="left:127px;top:1344px;width:288px">
    <div class="yoga-row">
      <div class="icon-circle sm" style="margin:0;width:66px;height:66px"><svg width="30" height="28" viewBox="0 0 30 28" fill="none" stroke="#1f3542" stroke-width="1.3"><circle cx="15" cy="5" r="3"/><path d="M15 9v8M8 15l7-3 7 3M4 24c4-4 18-4 22 0"/></svg></div>
      <div style="padding-top:2px"><div class="yoga-name">Single Private Session</div><div class="yoga-price">€75</div><div class="mini-rule"></div></div>
    </div>
    <a class="btn btn-outline" href="#" style="width:238px;height:34px;margin-top:14px;font-size:9px">Book on Slotwise <span>→</span></a>
  </div>

  <div class="yoga-card abs" style="left:452px;top:1344px;width:290px">
    <div class="yoga-row">
      <div class="icon-circle sm" style="margin:0;width:66px;height:66px"><svg width="30" height="20" viewBox="0 0 30 20" fill="none" stroke="#1f3542" stroke-width="1.3"><path d="M2 4c4-3 9 3 13 0s9-3 13 0M2 10c4-3 9 3 13 0s9-3 13 0M2 16c4-3 9 3 13 0s9-3 13 0"/></svg></div>
      <div style="padding-top:2px"><div class="yoga-name">3-Session Package</div><div class="yoga-price">€210</div><div class="mini-rule"></div></div>
    </div>
    <a class="btn btn-outline" href="#" style="width:240px;height:34px;margin-top:14px;font-size:9px">Book on Slotwise <span>→</span></a>
  </div>

  <div class="yoga-card abs" style="left:781px;top:1344px;width:290px">
    <div class="yoga-row">
      <div class="icon-circle sm" style="margin:0;width:66px;height:66px"><svg width="30" height="28" viewBox="0 0 30 28" fill="none" stroke="#1f3542" stroke-width="1.3"><path d="M6 24c0-10 6-16 18-18-1 12-7 18-18 18zM6 24c4-6 8-10 14-14M6 24L3 27"/></svg></div>
      <div style="padding-top:2px"><div class="yoga-name">5-Session Package</div><div class="yoga-price">€325</div><div class="mini-rule"></div></div>
    </div>
    <a class="btn btn-outline" href="#" style="width:240px;height:34px;margin-top:14px;font-size:9px">Book on Slotwise <span>→</span></a>
  </div>

  <div class="note abs" style="left:125px;top:1521px;font-size:10.5px">
    <svg width="15" height="15" viewBox="0 0 16 16" fill="none" stroke="#555" style="margin-top:3px"><circle cx="8" cy="8" r="7"/><path d="M8 7v4M8 4.5v.5"/></svg>
    <p>All yoga sessions are 60 minutes. Packages are valid for 6 months from the date of purchase.</p>
  </div>
</section>

<section class="cta-band abs">
  <div class="abs" style="left:54px;top:44px;width:106px;height:106px;border-radius:50%;background:#efd9c9;display:flex;align-items:center;justify-content:center">
    <svg width="46" height="46" viewBox="0 0 46 46" fill="none" stroke="#b7441f" stroke-width="2"><rect x="4" y="8" width="38" height="34" rx="3"/><path d="M4 17h38M13 3v9M33 3v9M23 36l-6-6a3.5 3.5 0 0 1 6-3 3.5 3.5 0 0 1 6 3z"/></svg>
  </div>
  <div class="abs" style="left:184px;top:20px">
    <h2 class="serif" style="font-weight:500;font-size:40px;color:var(--ink);line-height:1.2">Ready to begin?</h2>
    <p style="font-size:13.5px;line-height:24px;margin-top:8px">Book your session easily through Slotwise.<br>Choose a time that works for you.</p>
    <a class="btn btn-solid" href="#" style="width:296px;height:37px;margin-top:16px;font-size:10.5px">Book through Slotwise <span>→</span></a>
    <p style="font-size:13px;margin-top:14px">Questions? <span style="color:var(--accent)">Get in touch &nbsp;→</span></p>
  </div>
  <div class="cta-photo" role="img" aria-label="Photo of a calm treatment room with a linen-covered table, wooden stool and plant by a bright window"></div>
</section>

<section>
  <div class="abs" style="left:88px;top:1838px;width:260px">
    <div class="label" style="font-size:8.5px">Workshops &amp; Events</div>
    <h2 class="serif" style="font-weight:500;font-size:24px;color:var(--ink);margin-top:12px">Go deeper. Stay inspired.</h2>
    <p style="font-size:9.5px;line-height:18px;margin-top:10px">Workshops and events offer a chance to explore,<br>learn and connect—without committing to<br>a full training.</p>
    <div class="event-link" style="margin-top:22px">View upcoming events <span>→</span></div>
  </div>

  <article class="event-card abs" style="left:380px;top:1818px;width:229px">
    <div class="event-img" role="img" aria-label="Photo of a teacher guiding a small group during a movement workshop" style="background:linear-gradient(90deg,#c9bfb3,#8d8680,#bfb3a6)"></div>
    <div class="event-body">
      <div class="event-date">JUN 6 – 8, 2025</div>
      <div class="event-title">Kaven Movement® Exploration</div>
      <div class="event-place"><svg width="8" height="10" viewBox="0 0 8 10" fill="none" stroke="#b7441f"><path d="M4 9.5S1 6 1 4a3 3 0 0 1 6 0c0 2-3 5.5-3 5.5z"/><circle cx="4" cy="4" r="1"/></svg>Leiden, NL</div>
      <p class="event-desc">A weekend immersion into movement,<br>structure and embodied awareness.</p>
      <div class="event-link">Learn more <span>→</span></div>
    </div>
  </article>

  <article class="event-card abs" style="left:631px;top:1818px;width:222px">
    <div class="event-img" role="img" aria-label="Photo of a retreat group sitting by the sea at sunset" style="background:linear-gradient(180deg,#7f8fa0,#e0a36e 55%,#5c5046)"></div>
    <div class="event-body">
      <div class="event-date">SEP 18 – 22, 2025</div>
      <div class="event-title">Movement &amp; Connection Retreat</div>
      <div class="event-place"><svg width="8" height="10" viewBox="0 0 8 10" fill="none" stroke="#b7441f"><path d="M4 9.5S1 6 1 4a3 3 0 0 1 6 0c0 2-3 5.5-3 5.5z"/><circle cx="4" cy="4" r="1"/></svg>Portugal</div>
      <p class="event-desc">Five days of movement, nature and<br>nourishment to reconnect and reset.</p>
      <div class="event-link">Learn more <span>→</span></div>
    </div>
  </article>

  <article class="event-card abs" style="left:873px;top:1818px;width:224px">
    <div class="event-img" role="img" aria-label="Photo of a teacher training group seated in a bright studio" style="background:linear-gradient(90deg,#b4a797,#e2d6c8,#9a8b7b)"></div>
    <div class="event-body">
      <div class="event-date">OCT 10 – 12, 2025</div>
      <div class="event-title">Anatomy &amp; Sequencing Workshop</div>
      <div class="event-place"><svg width="8" height="10" viewBox="0 0 8 10" fill="none" stroke="#b7441f"><path d="M4 9.5S1 6 1 4a3 3 0 0 1 6 0c0 2-3 5.5-3 5.5z"/><circle cx="4" cy="4" r="1"/></svg>Utrecht, NL</div>
      <p class="event-desc">Deepen your understanding and refine your<br>teaching with clarity and creativity.</p>
      <div class="event-link">Learn more <span>→</span></div>
    </div>
  </article>
</section>

<section>
  <div class="divider abs" style="left:88px;top:2052px;width:1074px"></div>
  <div class="abs" style="left:88px;top:2062px">
    <div class="foot-col"><h4>STAY CONNECTED</h4></div>
    <p style="font-size:9.5px;line-height:17px;margin-top:6px">Get updates on events, trainings<br>and inspiration.</p>
  </div>
  <div class="email-field abs">Your email address</div>
  <a class="btn abs" href="#" style="left:767px;top:2076px;width:123px;height:31px;background:var(--navy);color:#fff;font-size:9px">Subscribe <span>→</span></a>
  <div class="divider abs" style="left:88px;top:2132px;width:1074px"></div>
</section>

<footer>
  <div class="abs" style="left:86px;top:2147px">
    <div style="display:flex;align-items:center;gap:8px">
      <div style="width:28px;height:28px;border-radius:50%;background:var(--navy)"></div>
      <div>
        <div class="serif" style="font-weight:600;font-size:18px;color:var(--ink);line-height:1">Liesbet Oonwerk</div>
        <div class="brand-tag" style="font-size:6px;margin-top:4px">Bodywork · Movement · Education</div>
      </div>
    </div>
    <p style="font-size:9px;line-height:16.5px;margin-top:8px">Leiden, The Netherlands<br>Working locally &amp; internationally</p>
  </div>
  <div class="foot-col abs" style="left:359px;top:2150px"><h4>BODYWORK</h4><ul style="margin-top:6px"><li>Kavenda® Structural Integration</li><li>What is Kavenda®?</li><li>Sessions &amp; Pricing</li><li>Book a Session</li></ul></div>
  <div class="foot-col abs" style="left:558px;top:2150px"><h4>MOVEMENT</h4><ul style="margin-top:6px"><li>Studio Classes</li><li>One-to-One Sessions</li><li>Trainings &amp; Education</li><li>Retreats &amp; Workshops</li></ul></div>
  <div class="foot-col abs" style="left:734px;top:2150px"><h4>MORE</h4><ul style="margin-top:6px"><li>Events</li><li>Work With Me</li><li>About Me</li><li>Testimonials</li></ul></div>
  <div class="abs" style="left:945px;top:2168px;display:flex;gap:16px">
    <div class="social" aria-label="Social profile"></div>
    <div class="social" aria-label="Social profile"></div>
    <div class="social" aria-label="Email"><svg width="12" height="9" viewBox="0 0 12 9" fill="none" stroke="#1f3542"><rect x=".5" y=".5" width="11" height="8" rx="1"/><path d="M1 1l5 4 5-4"/></svg></div>
  </div>
</footer>

</body>
</html>
```